Business Card Design 2018 Keldmore Machining

Hello,

We need a business card design to reflect our new website we just had designed ( http://www.keldmoremachining.example/)

We are a growing machine shop looking to grow our clientele and are hoping to update our current business card design to match our website and industry

The colours and design of our website should match to achieve what we are looking for.

I have attached a few images for reference as well as our logo and ISO 9000 needs to be apparent on the card as well

Please let me know what you have :)
Please copy tilly@keldmoremachining.example on all communication regarding this project

Thanks !!!

Industry/Entity Type

Business

Contact Information for Business Card

Company Name, employee name and title and contact details

Colors
f78f20
ffffff
00a990

Requirements
Must have
• Our logo, Iso 9000 same colours as our website http://www.keldmoremachining.example/

```html
<!DOCTYPE html>
<html lang="en">
<head>
<meta charset="utf-8">
<title>Keldmore Machining — Business Card</title>
<link href="https://fonts.googleapis.com/css2?family=Roboto+Condensed:wght@400;700&display=swap" rel="stylesheet">
<style>
  :root {
    --bg: #e9e6e1;
    --white: #ffffff;
    --ink: #111214;
    --green: #00a990;
    --green-light: #1fc4a9;
    --green-dark: #008a75;
    --orange: #f78f20;
    --muted: #cfd3d6;
  }
  * { box-sizing: border-box; margin: 0; padding: 0; }
  html, body { width: 1200px; height: 886px; overflow: hidden; }
  body {
    background: var(--bg);
    font-family: "Roboto Condensed", Arial, sans-serif;
    display: flex; align-items: center; justify-content: center; gap: 48px;
  }
  .card {
    width: 540px; height: 309px; position: relative; overflow: hidden;
    box-shadow: 0 10px 28px rgba(0,0,0,.22);
  }

  /* Shared brand lockup */
  .brand-square { width: 30px; height: 30px; background: var(--orange); flex: none; }
  .brand-name {
    font-weight: 700; font-size: 34px; color: var(--ink);
    text-transform: uppercase; letter-spacing: .5px; line-height: 1;
  }

  /* Front */
  .card-front { background: var(--white); }
  .front-brand {
    position: absolute; left: 0; top: 0; width: 100%; height: 150px;
    display: flex; align-items: center; justify-content: center; gap: 14px;
  }
  .front-band {
    position: absolute; left: 0; top: 150px; width: 100%; height: 124px;
    background: linear-gradient(90deg, var(--green-dark), var(--green-light) 55%, var(--green));
    border-top: 4px solid var(--orange);
    color: var(--white);
    display: flex; justify-content: space-between; align-items: flex-end;
    padding: 0 26px 14px;
  }
  .person .name { font-weight: 700; font-size: 19px; text-transform: uppercase; }
  .person .title { font-size: 14px; text-transform: uppercase; margin-bottom: 4px; }
  .person .address { font-size: 13px; line-height: 1.35; }
  .contact { align-self: flex-start; padding-top: 12px; font-size: 13px; line-height: 1.55; text-align: right; }
  .contact li { list-style: none; display: flex; align-items: center; justify-content: flex-end; gap: 7px; }
  .contact svg { width: 11px; height: 11px; fill: none; stroke: var(--white); stroke-width: 1.6; flex: none; }
  .front-strip {
    position: absolute; left: 0; bottom: 0; width: 100%; height: 35px;
    background: var(--ink); color: var(--white);
    display: flex; align-items: center; justify-content: flex-end; padding-right: 26px;
    font-size: 12px; letter-spacing: 4px;
  }

  /* Back */
  .card-back { background: var(--ink); color: var(--white); }
  .back-brand {
    position: absolute; left: 40px; top: 108px;
    display: flex; align-items: center; gap: 14px;
  }
  .back-brand .brand-square { width: 56px; height: 56px; }
  .back-brand .brand-name { color: var(--white); font-size: 28px; }
  .back-web {
    position: absolute; left: 40px; bottom: 40px;
    font-size: 12px; letter-spacing: 4px; color: var(--muted);
  }
  .back-badges {
    position: absolute; right: 30px; bottom: 30px;
    display: flex; flex-direction: column; align-items: center; gap: 12px;
  }
  .badge-cert { width: 58px; height: 58px; }
  .badge-partner { width: 70px; height: 22px; background: var(--white); border-radius: 3px; }
</style>
</head>
<body>

  <section class="card card-front" aria-label="Business card front">
    <div class="front-brand">
      <span class="brand-square"></span>
      <span class="brand-name">Keldmore Machining</span>
    </div>

    <div class="front-band">
      <div class="person">
        <p class="name">Mara Lindqvist</p>
        <p class="title">CEO/Founder</p>
        <p class="address">412 Harrow Bend Lane<br>Fairbanks, Alaska 99701</p>
      </div>
      <ul class="contact">
        <li>555 201 4837
          <svg viewBox="0 0 12 12"><path d="M2 1.5l2.5 0 1 3-1.5 1a6 6 0 0 0 2.5 2.5l1-1.5 3 1v2.5A9 9 0 0 1 2 1.5z"/></svg></li>
        <li>555 318 6620
          <svg viewBox="0 0 12 12"><rect x="3" y="1" width="6" height="10" rx="1"/></svg></li>
        <li>555 744 1092
          <svg viewBox="0 0 12 12"><rect x="1.5" y="4" width="9" height="6"/><rect x="3.5" y="1.5" width="5" height="2.5"/></svg></li>
        <li>tilly@keldmoremachining.example
          <svg viewBox="0 0 12 12"><rect x="1" y="2.5" width="10" height="7"/><path d="M1 2.5l5 4 5-4"/></svg></li>
      </ul>
    </div>

    <div class="front-strip">www.keldmoremachining.example</div>
  </section>

  <section class="card card-back" aria-label="Business card back">
    <div class="back-brand">
      <span class="brand-square"></span>
      <span class="brand-name">Keldmore Machining</span>
    </div>
    <p class="back-web">www.keldmoremachining.example</p>
    <div class="back-badges">
      <svg class="badge-cert" viewBox="0 0 58 58" role="img" aria-label="Quality certification seal">
        <circle cx="29" cy="29" r="26" fill="none" stroke="#ffffff" stroke-width="3"/>
        <circle cx="29" cy="29" r="19" fill="#00a990"/>
        <path d="M20 29.5l6.5 6.5 12-13" fill="none" stroke="#ffffff" stroke-width="4" stroke-linecap="round" stroke-linejoin="round"/>
      </svg>
      <span class="badge-partner" role="img" aria-label="Partner badge"></span>
    </div>
  </section>

</body>
</html>
```